Cell phone repair

you can please design me business card

size 3.5" x 2"

colors blue and red

fixit dash logo (you get from my website fixitdashhq.com )

"We Come To You!

It is very simple! You tell us what phone you have, And we come to fix it."

phone number: 412.586.3094

website: www.fixitdashhq.com

email: info@fixitdashhq.com

```html
<!DOCTYPE html>
<html lang="en">
<head>
<meta charset="utf-8">
<title>fixit dash – Business Card</title>
<link rel="stylesheet" href="https://fonts.googleapis.com/css2?family=Roboto:wght@500&family=Ribeye&family=Boogaloo&family=Roboto+Slab:wght@700&display=swap">
<style>
  :root {
    --page: #eceff2;
    --black: #0a0a0a;
    --red: #ee1c24;
    --blue: #1e7be0;
    --white: #ffffff;
    --ink: #111111;
    --line: #c9ccd2;
  }
  * { margin: 0; padding: 0; box-sizing: border-box; }
  html, body { width: 927px; height: 1200px; overflow: hidden; background: var(--page); }
  .canvas { position: relative; width: 927px; height: 1200px; }

  .card {
    position: absolute; left: 43px; width: 840px; height: 480px;
    background: var(--white); border: 4px solid var(--black); border-radius: 8px;
    overflow: hidden; box-shadow: 0 6px 18px rgba(0,0,0,.15);
  }
  .card--front { top: 90px; }
  .card--back { top: 640px; border-color: var(--line); }

  .card__top { position: absolute; left: 0; top: 0; width: 100%; height: 180px; background: var(--black); }
  .card__stripes { position: absolute; left: 0; top: 170px; }

  .brand { position: absolute; display: flex; align-items: center; gap: 14px; }
  .brand__name { font-family: "Roboto", sans-serif; font-weight: 500; color: var(--blue); letter-spacing: .5px; white-space: nowrap; }
  .brand__mark { background: var(--red); border-radius: 6px; }
  .card--front .brand { left: 105px; top: 62px; }
  .card--front .brand__name { font-size: 40px; }
  .card--front .brand__mark { width: 40px; height: 72px; }
  .card--back .brand { left: 50%; top: 50%; transform: translate(-50%, -50%); }
  .card--back .brand__name { font-size: 52px; }
  .card--back .brand__mark { width: 50px; height: 50px; }

  .tagline {
    position: absolute; left: 495px; top: 72px;
    font-family: "Ribeye", serif; font-size: 29px; color: var(--red); white-space: nowrap;
  }

  .pitch {
    position: absolute; right: 0; top: 150px; width: 330px; height: 106px;
    background: var(--red); clip-path: polygon(38px 0, 100% 0, 100% 100%, 38px 100%, 0 50%);
    display: flex; flex-direction: column; justify-content: center; align-items: center;
    font-family: "Boogaloo", cursive; font-size: 21px; line-height: 1.1; color: var(--white); text-align: center;
    padding-left: 30px; white-space: nowrap;
  }

  .card__photo {
    position: absolute; left: 10px; top: 195px; width: 385px; height: 275px;
    background: linear-gradient(120deg, #cfd3d8 0%, #eef0f3 40%, #9fc3ea 65%, #e4e6ea 100%);
    border-radius: 14px;
  }

  .contacts { position: absolute; left: 410px; top: 285px; list-style: none; }
  .contacts__item { display: flex; align-items: center; gap: 14px; height: 50px; margin-bottom: 8px; }
  .contacts__icon { flex: none; width: 44px; height: 44px; background: var(--black); border-radius: 6px; display: flex; align-items: center; justify-content: center; }
  .contacts__text { font-family: "Roboto Slab", serif; font-weight: 700; font-size: 16px; color: var(--ink); white-space: nowrap; }
</style>
</head>
<body>
<main class="canvas">

  <section class="card card--front">
    <div class="card__top"></div>
    <svg class="card__stripes" width="840" height="40" viewBox="0 0 840 40">
      <rect x="0" y="5" width="520" height="7" fill="#1e7be0"/>
      <rect x="0" y="16" width="500" height="5" fill="#ee1c24"/>
      <rect x="0" y="25" width="470" height="4" fill="#1e7be0"/>
      <rect x="0" y="32" width="440" height="3" fill="#ee1c24"/>
    </svg>

    <div class="brand">
      <span class="brand__name">fixit dash</span>
      <span class="brand__mark"></span>
    </div>

    <p class="tagline">"We Come To You!</p>

    <div class="pitch">
      <span>It is very simple!</span>
      <span>You tell us what phone you have,</span>
      <span>And we come to fix it."</span>
    </div>

    <div class="card__photo" role="img" aria-label="Photo of two smartphones, one with a cracked screen and one repaired"></div>

    <ul class="contacts">
      <li class="contacts__item">
        <span class="contacts__icon">
          <svg width="26" height="26" viewBox="0 0 24 24"><path fill="#fff" d="M6.6 10.8a15.1 15.1 0 0 0 6.6 6.6l2.2-2.2c.3-.3.7-.4 1-.2 1.1.4 2.3.6 3.6.6.6 0 1 .4 1 1V20c0 .6-.4 1-1 1A17 17 0 0 1 3 4c0-.6.4-1 1-1h3.5c.6 0 1 .4 1 1 0 1.3.2 2.5.6 3.6.1.3 0 .7-.2 1z"/></svg>
        </span>
        <span class="contacts__text">phone: 412.586.3094</span>
      </li>
      <li class="contacts__item">
        <span class="contacts__icon">
          <svg width="28" height="22" viewBox="0 0 28 22"><rect x="2" y="2" width="24" height="18" fill="none" stroke="#fff" stroke-width="2"/><path d="M2 2l12 10L26 2M2 20l9-9M26 20l-9-9" fill="none" stroke="#fff" stroke-width="2"/></svg>
        </span>
        <span class="contacts__text">email: info@fixitdashhq.com</span>
      </li>
      <li class="contacts__item">
        <span class="contacts__icon">
          <svg width="28" height="28" viewBox="0 0 28 28"><text x="14" y="21" text-anchor="middle" font-family="Arial, sans-serif" font-size="24" font-weight="700" fill="#fff">@</text></svg>
        </span>
        <span class="contacts__text">web: www.fixitdashhq.com</span>
      </li>
    </ul>
  </section>

  <section class="card card--back">
    <div class="brand">
      <span class="brand__name">fixit dash</span>
      <span class="brand__mark"></span>
    </div>
  </section>

</main>
</body>
</html>
```